Bright Harbor Homes
Stationary design for exciting new startup - Real Estate
Stationary design for exciting new startup
Professional
Dana Pruett
President
2475 Willowmere Blvd NW Suite 410 Marietta, GA 30062
dana.pruett@brightharborhomes.example
http://www.brightharborhomes.example

```html
<!DOCTYPE html>
<html lang="en">
<head>
<meta charset="utf-8">
<title>Bright Harbor Homes – Business Card</title>
<link rel="stylesheet" href="https://fonts.googleapis.com/css2?family=Cinzel:wght@500;600&family=Arimo:wght@400&display=swap">
<style>
  :root {
    --navy: #1c2d55;
    --navy-deep: #18264a;
    --green: #7cc23a;
    --green-light: #98d34e;
    --paper: #ffffff;
    --ink: #555b66;
    --rule: #d9dce1;
    --backdrop: #2a2a2c;
  }
  * { box-sizing: border-box; margin: 0; padding: 0; }
  html, body {
    width: 1200px; height: 750px; overflow: hidden;
    background: var(--backdrop);
  }
  .stage {
    position: relative; width: 1200px; height: 750px;
    display: flex; align-items: center; justify-content: center; gap: 40px;
  }
  .card {
    position: relative; width: 540px; height: 309px;
    border-radius: 16px; overflow: hidden;
  }
  .card--back {
    background: var(--navy);
    display: flex; align-items: center; justify-content: center;
  }
  .card--front { background: var(--paper); }

  .wordmark {
    font-family: "Cinzel", serif; font-weight: 600;
    text-align: center; line-height: 1.15;
    display: flex; align-items: center; gap: 12px;
  }
  .wordmark__dot {
    width: 18px; height: 18px; border-radius: 50%; flex: none;
  }
  .card--back .wordmark { color: var(--paper); font-size: 26px; }
  .card--back .wordmark__dot { background: var(--paper); }
  .card--front .wordmark {
    position: absolute; left: 34px; top: 118px; width: 240px;
    color: var(--navy); font-size: 22px;
  }
  .card--front .wordmark__dot { background: var(--green); }

  .card__band { position: absolute; inset: 0; }

  .divider {
    position: absolute; left: 296px; top: 36px; width: 1px; height: 140px;
    background: var(--rule);
  }
  .contact {
    position: absolute; left: 314px; top: 34px; width: 212px;
    font-family: "Arimo", sans-serif; color: var(--ink); font-size: 11px; line-height: 1.45;
  }
  .contact__name {
    font-family: "Cinzel", serif; font-weight: 600; font-size: 17px;
    color: var(--navy); line-height: 1.1;
  }
  .contact__title {
    font-family: "Cinzel", serif; font-weight: 600; font-size: 11px;
    color: var(--green); letter-spacing: 0.5px; margin-bottom: 8px;
  }
  .contact__address { margin-bottom: 10px; }
  .contact__line { display: flex; align-items: center; gap: 6px; }
  .contact__line svg { width: 10px; height: 10px; flex: none; fill: var(--green); }
  .contact__email { font-size: 10.3px; }
</style>
</head>
<body>
<main class="stage">
  <section class="card card--back" aria-label="Card back">
    <div class="wordmark"><span class="wordmark__dot"></span><span>Bright Harbor<br>Homes</span></div>
  </section>

  <section class="card card--front" aria-label="Card front">
    <svg class="card__band" viewBox="0 0 540 309" width="540" height="309" aria-hidden="false">
      <polygon points="0,284 540,172 540,309 0,309" fill="var(--green)"/>
      <polygon points="0,284 540,172 540,182 0,294" fill="var(--green-light)"/>
      <polygon points="0,252 62,309 0,309" fill="var(--navy-deep)"/>
      <text x="250" y="262" transform="rotate(-11.7 250 262)"
            font-family="Cinzel, serif" font-weight="600" font-size="12.5"
            letter-spacing="0.6" fill="var(--navy)">WWW.BRIGHTHARBORHOMES.EXAMPLE</text>
    </svg>

    <div class="wordmark"><span class="wordmark__dot"></span><span>Bright Harbor<br>Homes</span></div>

    <div class="divider"></div>

    <div class="contact">
      <p class="contact__name">Dana Pruett</p>
      <p class="contact__title">PRESIDENT</p>
      <p class="contact__address">2475 Willowmere Blvd NW<br>Suite 410, Marietta, GA 30062</p>
      <p class="contact__line">
        <svg viewBox="0 0 10 10"><path d="M2 0.5 L3.6 0.5 L4.2 2.8 L3 3.6 Q4 6 6.4 7 L7.2 5.8 L9.5 6.4 L9.5 8 Q9.5 9.5 8 9.5 Q1 9 0.5 2 Q0.5 0.5 2 0.5Z"/></svg>
        <span>678-555-0142</span>
      </p>
      <p class="contact__line">
        <svg viewBox="0 0 10 10"><path d="M3 0 H7 Q8 0 8 1 V9 Q8 10 7 10 H3 Q2 10 2 9 V1 Q2 0 3 0Z M3 1.5 V7.5 H7 V1.5Z"/></svg>
        <span>404-555-0187</span>
      </p>
      <p class="contact__line contact__email">
        <svg viewBox="0 0 10 10"><path d="M0 2 H10 V8 H0Z M0.8 2.6 L5 5.6 L9.2 2.6" stroke="#fff" stroke-width="0.8"/></svg>
        <span>dana.pruett@brightharborhomes.example</span>
      </p>
    </div>
  </section>
</main>
</body>
</html>
```